VineGlow Artbook for Okanagan Region, British Columbia

Creating an art book: VineGlow, for the Okanagan Wine Region in British Columbia, Canada. Would like smart, modern, clean and linear...cool, sexy urban, not ugly boring suburban... I need a cover that appeals to the wino in all of us! Title: VineGlow -Marla Pettivan
Updates
Thank you all kindly for your efforts. I have added some files so that you can get a sense of my aesthetic...it's never easy trying to figure it out, is it? I will hopefully have dimensions of book soon...cheers, Marla
would anyone please design a giant wine bottle with the wine label that looks like a label but says vineglow...just curious to see if it works as a design or not...thank you.
Target Market(s)
Designing this wine art book of quotes to wineries in Okanagan BC. Buyer is wine lover and tourist ready to spend his vacation bucks on this wonderful book!
Look and feel

```html
<!DOCTYPE html>
<html lang="en">
<head>
<meta charset="utf-8">
<title>VineGlow — Marla Pettivan</title>
<link rel="stylesheet" href="https://fonts.googleapis.com/css2?family=Oswald:wght@700&family=Raleway:wght@300&display=swap">
<style>
  :root {
    --page-bg: #f4f2ef;
    --cover-brown: #55260a;
    --cork-pale: #f0cfae;
    --cork-light: #dfae84;
    --cork-mid: #c48552;
    --cork-deep: #7d3f18;
    --cork-shadow: #4a1d06;
    --author-ink: #f1e6da;
    --title-ink: #4a1f08;
    --seal-face: #ecc7a2;
  }
  * { margin: 0; padding: 0; box-sizing: border-box; }
  html, body {
    width: 1200px;
    height: 907px;
    overflow: hidden;
    background: var(--page-bg);
  }
  .stage {
    width: 1200px;
    height: 907px;
    display: flex;
    align-items: center;
    justify-content: center;
  }
  .book-cover {
    position: relative;
    width: 480px;
    height: 770px;
    background: var(--cover-brown);
    overflow: hidden;
  }
  .author-name {
    position: absolute;
    top: 62px;
    left: 0;
    right: 0;
    text-align: center;
    font-family: "Raleway", sans-serif;
    font-weight: 300;
    font-size: 15px;
    letter-spacing: 0.8em;
    padding-left: 0.8em;
    text-transform: uppercase;
    color: var(--author-ink);
  }
  .cork-photo {
    position: absolute;
    left: 0;
    right: 0;
    top: 250px;
    bottom: 0;
    background:
      radial-gradient(ellipse 30% 22% at 14% 18%, var(--cork-light) 0%, rgba(223,174,132,0) 100%),
      radial-gradient(ellipse 28% 20% at 86% 14%, var(--cork-light) 0%, rgba(223,174,132,0) 100%),
      radial-gradient(ellipse 30% 25% at 88% 58%, var(--cork-mid) 0%, rgba(196,133,82,0) 100%),
      radial-gradient(ellipse 26% 40% at 12% 75%, var(--cork-mid) 0%, rgba(196,133,82,0) 100%),
      radial-gradient(ellipse 40% 35% at 50% 50%, var(--cork-pale) 0%, rgba(240,207,174,0) 100%),
      linear-gradient(180deg, var(--cover-brown) 0%, var(--cork-deep) 10%, var(--cork-mid) 35%, var(--cork-light) 60%, var(--cork-mid) 85%, var(--cork-shadow) 100%);
  }
  .title-seal {
    position: absolute;
    left: 50%;
    top: 467px;
    width: 220px;
    height: 220px;
    margin-left: -110px;
    margin-top: -110px;
    border-radius: 50%;
    background: var(--seal-face);
  }
  .cover-title {
    position: absolute;
    top: 467px;
    left: 0;
    right: 0;
    transform: translateY(-50%);
    text-align: center;
    font-family: "Oswald", sans-serif;
    font-weight: 700;
    font-size: 46px;
    line-height: 1;
    letter-spacing: -0.01em;
    color: var(--title-ink);
  }
</style>
</head>
<body>
  <main class="stage">
    <section class="book-cover">
      <p class="author-name">Marla Pettivan</p>
      <div class="cork-photo" role="img" aria-label="Close-up photograph of a heap of wine corks in warm tan tones, one cork end facing the viewer"></div>
      <div class="title-seal"></div>
      <h1 class="cover-title">VineGlow</h1>
    </section>
  </main>
</body>
</html>
```